Brindle Works Australia Website

Brindle Works Australia (BWA) is a Industrial, Mining & Transport Services provider in Australia. We require a website that is both pc and mobile freindly. The website will be used to both present our company services and give us exposure in a crowded market. The main page of the website will have a snapshot of who BWA is and its from this page that the user can click to enter the area of interest ie. Industrial, Mining and Transport. A disticted logo can be used to indicate the area in question.<br/>Within the industrial, Mining and the Transport services pages will need list and description of services that are provided, current customer lists and news pages.<br/>The website will need a contacts page so prospective customers can get in contact with BWA.<br/>The website design will require a user freindly back end so future updates and ammendments can be carriedout by less experienced people within the BWA business.

Target Market(s)

Industrial, Mining and Transport Services provider markets

Coding

Coded - Design and coding required

Number of Pages Required

5+ page

Font styles to use
Sans Serif

Colors
00a990

Requirements
Must have
• Ability to build servises with in services. because the main service area is only the main service with in each service group there is alot of smaller services / tasks.
• Key wording for easy seach engine capabilities. The website will need to be search engine freindly.

```html
<!DOCTYPE html>
<html lang="en">
<head>
<meta charset="utf-8">
<title>Brindle Works Australia — Mining &amp; Transport</title>
<link href="https://fonts.googleapis.com/css2?family=Lato:wght@300;400;700&family=Antonio:wght@400&display=swap" rel="stylesheet">
<style>
:root{
  --teal:#00a990;
  --gold:#f2c200;
  --white:#ffffff;
  --ink:#000000;
  --dark:#1c1d1f;
  --earth-1:#5a3a22;
  --earth-2:#3a2616;
  --cave-1:#2a231d;
  --cave-2:#151210;
}
*{margin:0;padding:0;box-sizing:border-box}
html,body{width:1200px;height:2848px;overflow:hidden}
body{font-family:'Lato',sans-serif;color:var(--white);background:var(--dark);position:relative}
section{position:absolute;left:0;width:1200px;overflow:hidden}

/* Hero */
.hero{top:0;height:747px;background:radial-gradient(ellipse at 45% 50%,#6e4b2f 0%,var(--earth-1) 45%,var(--earth-2) 100%)}
.brand{position:absolute;top:215px;left:0;width:1200px;display:flex;justify-content:center;align-items:center;gap:14px}
.brand-mark{font-family:'Lato',sans-serif;font-weight:700;font-size:58px;letter-spacing:-1px;color:var(--white)}
.brand-name{font-family:'Lato',sans-serif;font-weight:700;font-size:22px;line-height:22px;color:var(--white);text-transform:uppercase}
.hero-title{position:absolute;top:290px;width:1200px;text-align:center;font-family:'Antonio',sans-serif;font-weight:400;font-size:72px;letter-spacing:0;line-height:76px}
.hero-sub{position:absolute;top:371px;width:1200px;text-align:center;font-size:15px}
.btn-sectors{position:absolute;top:436px;left:554px;width:91px;height:28px;border-radius:14px;background:var(--teal);font-size:9px;line-height:28px;text-align:center;text-transform:uppercase}
.scroll{position:absolute;top:662px;left:550px;width:100px;text-align:center;font-size:10px;white-space:nowrap}
.scroll svg{display:block;margin:0 auto}

/* Sectors */
.sectors{top:747px;height:268px;display:flex}
.sector{position:relative;height:268px}
.sector:nth-child(1){width:404px;background:linear-gradient(180deg,#4f6277 0%,#3a3a30 60%,#2b2720 100%)}
.sector:nth-child(2){width:414px;background:linear-gradient(120deg,#2a2222 0%,#4a2a1e 55%,#2a1c18 100%)}
.sector:nth-child(3){width:382px;background:linear-gradient(180deg,#56616a 0%,#3f3d33 60%,#2c2a23 100%)}
.sector-icon{position:absolute;left:54px;top:82px}
.sector-title{position:absolute;left:54px;top:120px;font-size:23px;font-weight:400}
.sector-rule{position:absolute;left:54px;top:168px;width:48px;height:1px;background:rgba(255,255,255,.6)}
.sector-text{position:absolute;left:54px;top:182px;width:300px;font-size:10px;line-height:16px}

/* News */
.news{top:1015px;height:621px;background:var(--teal)}
.section-title{position:absolute;width:1200px;text-align:center;font-weight:400;font-size:33px}
.section-rule{position:absolute;left:544px;width:112px;height:1px;background:rgba(255,255,255,.6)}
.news .section-title{top:82px}
.news .section-rule{top:142px}
.news-grid{position:absolute;left:162px;top:183px;width:876px;display:grid;grid-template-columns:repeat(4,219px);grid-template-rows:repeat(2,187px)}
.news-photo{background:linear-gradient(160deg,#3f5f8a 0%,#6d6a62 45%,#8a6a32 75%,#4b3d2a 100%)}
.news-card{background:var(--ink);display:flex;flex-direction:column;align-items:center;justify-content:center;text-align:center;padding:0 42px}
.news-tag{color:var(--teal);font-size:10px;letter-spacing:2.5px;margin-bottom:12px}
.news-text{font-size:8.5px;line-height:15px;margin-bottom:12px}
.news-link{color:var(--gold);font-size:14px;letter-spacing:3px}
.news-frame{position:absolute;left:612px;top:1398px;width:412px;height:161px;border:1px solid var(--gold)}

/* Contact */
.contact{top:1636px;height:749px;background:radial-gradient(ellipse at 75% 55%,#3a3530 0%,var(--cave-1) 40%,var(--cave-2) 100%)}
.contact .section-title{top:176px}
.contact .section-rule{top:236px}
.field{position:absolute;height:37px;border:1.5px solid var(--gold);font-size:9px;letter-spacing:2px;padding:13px 13px 0}
.field.select::after{content:"";position:absolute;right:13px;top:16px;border:4px solid transparent;border-top-color:var(--white)}
.field.area{height:140px;padding-top:18px}

/* Connect */
.connect{top:2385px;height:463px;background:linear-gradient(180deg,#242527 0%,#1f2022 60%,#191a1c 100%)}
.connect .section-title{top:85px;font-weight:300;font-size:36px}
.connect .section-rule{top:143px}
.socials{position:absolute;top:2558px;left:478px;display:flex;gap:13px}
.social{width:36px;height:36px;border-radius:50%;background:var(--white);display:flex;align-items:center;justify-content:center}
.social::after{content:"";width:8px;height:8px;border-radius:50%;background:#3a3b3e}
.subscribe{position:absolute;top:2630px;left:330px;width:540px;height:55px;background:var(--white);color:var(--ink)}
.subscribe-label{position:absolute;left:21px;top:21px;font-size:9px}
.subscribe-btn{position:absolute;left:389px;top:11px;width:133px;height:33px;background:var(--gold);color:var(--white);font-size:8px;display:flex;align-items:center;justify-content:center;gap:8px}
</style>
</head>
<body>

<section class="hero" role="img" aria-label="Aerial photo of an open-cut mine site with haul trucks">
  <div class="brand"><span class="brand-mark">BWA</span><span class="brand-name">Brindle Works<br>Australia</span></div>
  <h1 class="hero-title">MINING &amp; TRANSPORT</h1>
  <p class="hero-sub">Austrailian Expert Control Services</p>
  <div class="btn-sectors">Our Sectors</div>
  <div class="scroll">
    <svg width="20" height="34" viewBox="0 0 20 34"><rect x="1" y="1" width="18" height="32" rx="9" fill="none" stroke="#fff" stroke-width="1.5"/><line x1="10" y1="7" x2="10" y2="13" stroke="#fff" stroke-width="1.5"/></svg>
    <div>Scroll Down</div>
    <svg width="10" height="6" viewBox="0 0 10 6"><polyline points="1,1 5,5 9,1" fill="none" stroke="#fff" stroke-width="1.2"/></svg>
  </div>
</section>

<section class="sectors">
  <div class="sector" role="img" aria-label="Photo of a mining haul truck under a cloudy sky">
    <svg class="sector-icon" width="64" height="34" viewBox="0 0 64 34" aria-label="Truck icon">
      <path d="M2 6 H40 V24 H2 Z" fill="#fff"/>
      <path d="M42 10 H54 L62 18 V24 H42 Z" fill="#fff"/>
      <circle cx="12" cy="27" r="5" fill="#fff" stroke="#444" stroke-width="2"/>
      <circle cx="26" cy="27" r="5" fill="#fff" stroke="#444" stroke-width="2"/>
      <circle cx="52" cy="27" r="5" fill="#fff" stroke="#444" stroke-width="2"/>
    </svg>
    <h2 class="sector-title">Tranportation</h2>
    <p class="sector-text">Lorem ipsum dolor sit amet, consectetuer adipiscing elit. Donec odio. Quisque volutpat mattis eros posuere a, pede.</p>
  </div>
  <div class="sector" role="img" aria-label="Photo of a worker in orange high-visibility gear">
    <svg class="sector-icon" style="top:72px" width="40" height="46" viewBox="0 0 40 46" aria-label="Factory icon">
      <path d="M2 46 V22 L12 16 V22 L22 16 V22 L28 18 V6 H34 V46 Z" fill="#fff"/>
      <rect x="7" y="30" width="5" height="5" fill="#3a2620"/>
      <rect x="15" y="30" width="5" height="5" fill="#3a2620"/>
      <rect x="23" y="30" width="5" height="5" fill="#3a2620"/>
      <circle cx="36" cy="4" r="4" fill="#fff"/>
    </svg>
    <h2 class="sector-title">Industrial</h2>
    <div class="sector-rule"></div>
    <p class="sector-text">Lorem ipsum dolor sit amet, consectetuer adipiscing elit. Donec odio. Quisque volutpat mattis eros posuere a, pede.</p>
  </div>
  <div class="sector" role="img" aria-label="Photo of earth moving machinery at a quarry">
    <svg class="sector-icon" style="top:66px;left:62px" width="84" height="46" viewBox="0 0 84 46" aria-label="Bulldozer icon">
      <path d="M14 4 H34 V20 H50 V30 H6 V20 H14 Z" fill="#fff"/>
      <path d="M62 18 L74 30 H84 V40 H64 L56 28 Z" fill="#fff"/>
      <rect x="2" y="32" width="52" height="12" rx="6" fill="#fff"/>
      <circle cx="12" cy="38" r="2.5" fill="#444"/>
      <circle cx="22" cy="38" r="2.5" fill="#444"/>
      <circle cx="32" cy="38" r="2.5" fill="#444"/>
      <circle cx="42" cy="38" r="2.5" fill="#444"/>
    </svg>
    <h2 class="sector-title" style="top:126px">Earth Movers</h2>
    <div class="sector-rule"></div>
    <p class="sector-text">Lorem ipsum dolor sit amet, consectetuer adipiscing elit. Donec odio. Quisque volutpat mattis eros posuere a, pede.</p>
  </div>
</section>

<section class="news">
  <h2 class="section-title">In the News</h2>
  <div class="section-rule"></div>
  <div class="news-grid">
    <div class="news-photo" role="img" aria-label="Photo of a haul truck at an open-pit mine"></div>
    <div class="news-card"><p class="news-tag">LOREM IPSUM</p><p class="news-text">Praesent dapibus, neque id cursus faucibus, tortor neque egestas</p><p class="news-link">READ MORE</p></div>
    <div class="news-photo" role="img" aria-label="Photo of a haul truck at an open-pit mine"></div>
    <div class="news-card"><p class="news-tag">LOREM IPSUM</p><p class="news-text">Nam dui mi, tincidunt quis, accumsan porttitor, facilisis luctus, metus.</p><p class="news-link">READ MORE</p></div>
    <div class="news-card"><p class="news-tag">LOREM IPSUM</p><p class="news-text">Phasellus ultrices nulla quis nibh. Quisque a lectus.</p><p class="news-link">READ MORE</p></div>
    <div class="news-photo" role="img" aria-label="Photo of a haul truck at an open-pit mine"></div>
    <div class="news-card"><p class="news-tag">LOREM IPSUM</p><p class="news-text">Phasellus ultrices nulla quis nibh. Quisque a lectus.</p><p class="news-link">READ MORE</p></div>
    <div class="news-photo" role="img" aria-label="Photo of a haul truck at an open-pit mine"></div>
  </div>
</section>
<div class="news-frame"></div>

<section class="contact" role="img" aria-label="Photo of a backhoe loader inside an underground mine tunnel">
  <h2 class="section-title">Contact Us Now</h2>
  <div class="section-rule"></div>
  <div class="field" style="left:254px;top:290px;width:322px">Name*</div>
  <div class="field" style="left:611px;top:290px;width:321px">Email *</div>
  <div class="field" style="left:254px;top:341px;width:145px">Phone *</div>
  <div class="field" style="left:432px;top:341px;width:143px">Seats*</div>
  <div class="field select" style="left:611px;top:341px;width:142px">Date*</div>
  <div class="field select" style="left:790px;top:341px;width:142px">Time*</div>
  <div class="field area" style="left:254px;top:405px;width:678px">Request for Vip *</div>
</section>

<section class="connect">
  <h2 class="section-title">Connect with us</h2>
  <div class="section-rule"></div>
</section>
<div class="socials">
  <div class="social"></div><div class="social"></div><div class="social"></div><div class="social"></div><div class="social"></div>
</div>
<div class="subscribe">
  <span class="subscribe-label">Enter Your Email</span>
  <div class="subscribe-btn">Subcribe
    <svg width="9" height="9" viewBox="0 0 10 10"><polygon points="0,5 10,0 7,10 5,6" fill="#fff"/></svg>
  </div>
</div>

</body>
</html>
```